KTRWG Promotion Flyer to raise money and communicate our goals

We need a flyer that promotes our organization. We are a 501(c)3 trying to raise money for Arts, Education and Entrepreneurship in our small town.

We promote a social events that improve qualtiy of life and educate people on how to start and expand businesses. Our goal is to make downtown an active and thriving place with many things for people to do and enjoy as well as create a favorable place for business.

Target Market(s)

Wealthy donors and Organizations with cash

Industry/Entity Type

Education

Colors

Designer to choose colors to be used in the design.

Requirements
Must have
• Eye catching graphics and look very professional
• Should appeal to men and women
Nice to have
• Make use of any known psychological colors and fonts etc... that appeal to philanthropic people
Should not have
• Should not be complicated or confusing

```html
<!DOCTYPE html>
<html lang="en">
<head>
<meta charset="utf-8">
<title>KTRWG Membership Flyer</title>
<link href="https://fonts.googleapis.com/css2?family=Raleway:wght@400;500;700;800&family=Arimo:wght@700&family=Cabin+Sketch:wght@700&display=swap" rel="stylesheet">
<style>
  :root {
    --pink: #e8327c;
    --blue: #3d8fc9;
    --light-blue: #8fd0f2;
    --green: #b4c92f;
    --gray: #8f8f8f;
    --text: #4a4a4a;
    --dark: #2b2b2b;
    --white: #ffffff;
    --sky-top: #5d8fc2;
    --sky-mid: #b9cfe3;
    --rock: #2f3338;
  }
  * { margin: 0; padding: 0; box-sizing: border-box; }
  html, body { width: 856px; height: 1200px; overflow: hidden; background: var(--white); }
  .flyer {
    position: relative;
    width: 856px;
    height: 1200px;
    overflow: hidden;
    background: var(--white);
    font-family: "Raleway", sans-serif;
    color: var(--text);
  }
  .hero {
    position: absolute;
    left: 0; top: 0;
    width: 856px; height: 515px;
    background:
      radial-gradient(circle at 64% 18%, rgba(255,255,255,0.95) 0, rgba(255,255,255,0.4) 70px, rgba(255,255,255,0) 180px),
      linear-gradient(180deg, var(--sky-top) 0%, var(--sky-mid) 55%, #7f8a96 75%, var(--rock) 100%);
  }
  .hero-frame { position: absolute; left: 0; top: 0; }
  .brand {
    position: absolute;
    left: 46px; top: 62px;
    width: 190px;
    text-align: center;
  }
  .brand-mark {
    display: block;
    width: 34px; height: 34px;
    margin: 0 auto 10px;
    background: var(--blue);
  }
  .brand-name {
    display: block;
    font-weight: 800;
    font-size: 30px;
    letter-spacing: 2px;
    color: var(--dark);
    line-height: 1;
  }
  .headline {
    position: absolute;
    left: 200px; top: 70px;
    width: 460px;
    text-align: center;
    font-family: "Cabin Sketch", cursive;
    font-weight: 700;
    line-height: 1;
    text-shadow: 0 2px 3px rgba(0,0,0,0.25);
  }
  .headline span { display: block; }
  .headline .l-big { font-size: 64px; color: var(--white); height: 62px; }
  .headline .l-things { font-size: 86px; color: var(--green); height: 84px; }
  .headline .l-often { font-size: 60px; color: var(--white); height: 64px; }
  .headline .l-have { font-size: 72px; color: var(--light-blue); height: 64px; }
  .headline .l-small { font-size: 62px; color: var(--white); letter-spacing: 4px; height: 60px; }
  .headline .l-beginnings { font-size: 78px; color: var(--pink); margin-left: -60px; }
  .intro {
    position: absolute;
    left: 37px; top: 536px;
    width: 780px;
    font-family: "Arimo", sans-serif;
    font-weight: 700;
    font-size: 15.3px;
    line-height: 20.5px;
    color: var(--dark);
  }
  .services { list-style: none; }
  .service {
    position: absolute;
    left: 36px;
    width: 390px;
    padding-left: 55px;
    min-height: 76px;
  }
  .service--promote { top: 656px; }
  .service--provide { top: 750px; }
  .service--help { top: 833px; }
  .service--work { top: 915px; }
  .service-icon {
    position: absolute;
    left: 0; top: 0;
    width: 40px; height: 76px;
    display: flex; align-items: flex-start; justify-content: center;
    padding-top: 10px;
  }
  .service-icon svg { width: 24px; height: 24px; }
  .service--promote .service-icon { background: var(--green); }
  .service--provide .service-icon { background: var(--blue); }
  .service--help .service-icon { background: var(--pink); }
  .service--work .service-icon { background: var(--gray); }
  .service-title {
    font-weight: 400;
    font-size: 22px;
    line-height: 1;
    color: var(--gray);
    letter-spacing: 0.3px;
  }
  .service-title strong { font-weight: 800; }
  .service--promote strong { color: var(--green); }
  .service--provide strong { color: var(--blue); }
  .service--help strong { color: var(--pink); }
  .service--work strong { color: #a8a8a8; }
  .service--work .service-text { margin-top: 9px; }
  .service-text {
    font-weight: 500;
    font-size: 15.2px;
    line-height: 20.5px;
    color: var(--text);
    margin-top: 2px;
    hyphens: auto;
  }
  .appeal {
    position: absolute;
    left: 457px; top: 656px;
    width: 346px;
    font-weight: 500;
    font-size: 15.2px;
    line-height: 20.5px;
    color: var(--text);
    text-align: justify;
    hyphens: auto;
  }
  .appeal p { margin-bottom: 13px; }
  .appeal strong { font-weight: 800; color: var(--dark); }
  .appeal .call {
    font-weight: 700;
    font-style: italic;
    font-size: 16.5px;
    color: var(--green);
    text-align: left;
  }
  .color-band {
    position: absolute;
    left: 0; top: 1024px;
    width: 856px; height: 29px;
    display: flex;
  }
  .color-band span { flex: 1; }
  .color-band .c-pink { background: var(--pink); }
  .color-band .c-blue { background: var(--blue); }
  .color-band .c-green { background: var(--green); }
  .color-band .c-gray { background: var(--gray); }
  .town-strip {
    position: absolute;
    left: 0; top: 1053px;
    width: 856px; height: 147px;
    background: linear-gradient(180deg, #c9d7e4 0%, #9fb4c6 45%, #8b7c68 75%, #6d6a5e 100%);
  }
</style>
</head>
<body>
<div class="flyer">

  <div class="hero" role="img" aria-label="Photograph of two hikers helping each other up a rocky summit against a bright sunny sky, overlaid with sketched small-town storefronts"></div>

  <svg class="hero-frame" width="856" height="240" viewBox="0 0 856 240" aria-hidden="true">
    <polygon points="380,0 856,0 856,46" fill="var(--pink)"/>
    <polygon points="0,128 0,166 36,148" fill="var(--green)"/>
    <polygon points="0,0 402,0 163,226 0,124" fill="var(--white)"/>
  </svg>

  <div class="brand">
    <span class="brand-mark"></span>
    <span class="brand-name">KTRWG</span>
  </div>

  <h1 class="headline">
    <span class="l-big">Big</span>
    <span class="l-things">things</span>
    <span class="l-often">often</span>
    <span class="l-have">have</span>
    <span class="l-small">SMALL</span>
    <span class="l-beginnings">beginnings</span>
  </h1>

  <p class="intro">The Larkhaven Small Business Association (KTRWG) is a local leader in the areas of Arts, Education and Entrepreneurship and is working diligently to promote Larkhaven and revitalize our downtown. When you become an KTRWG Member, you will be a part of the citywide work that the KTRWG does every day to improve the lives of citizens of Larkhaven:</p>

  <ul class="services">
    <li class="service service--promote">
      <div class="service-icon">
        <svg viewBox="0 0 24 24" fill="none" stroke="#fff" stroke-width="2" stroke-linejoin="round"><path d="M3 9h4l8-5v16l-8-5H3z" fill="#fff"/><path d="M18 9c1.5 1 1.5 5 0 6M20 7c3 2 3 8 0 10"/></svg>
      </div>
      <p class="service-title">WE <strong>PROMOTE</strong></p>
      <p class="service-text">Larkhaven Hotels, Shopping and Events that make Larkhaven a pleasant, exciting and prosperous place to live.</p>
    </li>
    <li class="service service--provide">
      <div class="service-icon">
        <svg viewBox="0 0 24 24" fill="none" stroke="#fff" stroke-width="1.8"><rect x="9" y="3" width="12" height="9"/><circle cx="5" cy="7" r="2" fill="#fff"/><path d="M5 10v10M3 20h4M5 12l5-2M15 12v8"/></svg>
      </div>
      <p class="service-title">WE <strong>PROVIDE</strong></p>
      <p class="service-text">training and resources to anyone interested Arts, Education and Entrepreneurship.</p>
    </li>
    <li class="service service--help">
      <div class="service-icon">
        <svg viewBox="0 0 24 24" fill="none" stroke="#fff" stroke-width="1.6"><rect x="4" y="2" width="16" height="20"/><path d="M7 7h10M7 11h10M7 15h6M7 18h8"/></svg>
      </div>
      <p class="service-title">WE <strong>HELP</strong></p>
      <p class="service-text">entrepreneur's start and grow their business&shy;es in a tax efficient and appropriate way.</p>
    </li>
    <li class="service service--work">
      <div class="service-icon">
        <svg viewBox="0 0 24 24" fill="#fff"><rect x="3" y="15" width="3" height="6"/><rect x="8" y="12" width="3" height="9"/><rect x="13" y="9" width="3" height="12"/><rect x="18" y="5" width="3" height="16"/><path d="M14 4l5-2 1 5z"/></svg>
      </div>
      <p class="service-title">WE <strong>WORK</strong></p>
      <p class="service-text">with all levels of local government to promote our community and create a fertile environ&shy;ment for growth.</p>
    </li>
  </ul>

  <div class="appeal">
    <p>Every day, we look for ways to help our local businesses grow and expand, but we need you by our side.</p>
    <p><strong>As an KTRWG Member,</strong> you can help provide training, education and support, and you can give our many businesses a chance to grow and our citizens the opportunity to experience big town amenities and events in a small town. Members' regular monthly gifts provide a consistent, reliable income stream that allows us to spend less time fundraising—and more time helping our businesses and community.</p>
    <p>Becoming an KTRWG Member is an easy, efficient and tax-deductible way to make a difference for our community all year long.</p>
    <p class="call">Please donate today.</p>
  </div>

  <div class="color-band" aria-hidden="true">
    <span class="c-pink"></span><span class="c-blue"></span><span class="c-green"></span><span class="c-gray"></span>
  </div>

  <div class="town-strip" role="img" aria-label="Strip of town photographs in tinted vertical slices: an open pavilion, a welcome sign, a park with a walking path, a trail head park sign and a downtown sidewalk"></div>

</div>
</body>
</html>
```